Website design for respected, long standing real estate development company in Central Oregon

Uncoded PSD design only. Homepage and one interior sample page.

Updated website design needed for Fenwick Holdings, one of Central Oregon’s oldest and most respected real estate development companies. They develop communities that focus on natural beauty and upscale amenities.

They need a website that features their long, unique history and their current efforts to build smart, healthy and livable communities. They need to tell their story to those who aren't familiar with the company. They need to build credibility and set themselves apart from other real estate development companies.

Current site: http://fenwick-holdings.example/

Target Market(s)

Target market is people who are new or plan to relocate to Central Oregon and are researching communities they want to live in.
Secondary markets are potential project partners, and the media. They need to build credibility with these audiences.
The site also needs to be easy to use for non-profits seeking contributions.

Industry/Entity Type

Real Estate Development

Number of Pages Required

2 page

Font styles to use
Sans Serif

Requirements
Must have
• Must have simple, user-friendly navigation with organized content.
• Design must be fresh, light and modern.
• Design must use great, high impact imagery that promotes the Central Oregon lifestyle.
• Design must highlight current and future communities and encourage click-throughs to those specific websites.
• Include video element.
• Include social links.
• Do not use dummy copy/lorum ipsum. Use copy from the current site instead. Use correct phone number, address, etc.
Should not have
• Lorum ipsum/dummy copy

```html
<!DOCTYPE html>
<html lang="en">
<head>
<meta charset="utf-8">
<title>Fenwick Holdings – Home</title>
<link rel="stylesheet" href="https://fonts.googleapis.com/css2?family=Bebas+Neue&family=Open+Sans:wght@400;600;700&family=Raleway:wght@400;500&family=Roboto+Condensed:wght@400&display=swap">
<style>
:root{
  --plum:#44203d;
  --ink:#3a3a3a;
  --text:#555;
  --topbar:#eceef2;
  --band:#d9d9d9;
  --soft:#efefef;
  --footer:#e8e8e8;
  --white:#fff;
}
*{box-sizing:border-box;margin:0;padding:0}
html,body{width:1200px;height:2381px;overflow:hidden}
body{font-family:"Open Sans",sans-serif;color:var(--text);background:var(--white);position:relative}

.topbar{position:absolute;left:0;top:0;width:1200px;height:41px;background:var(--topbar);border-bottom:1px solid #dcdde2}
.social{display:flex;gap:22px;align-items:center}
.social span{width:14px;height:14px;border-radius:50%;background:var(--ink);display:block}
.topbar .social{position:absolute;left:76px;top:14px}
.topbar .phone{position:absolute;right:79px;top:8px;font:700 21px "Open Sans",sans-serif;color:var(--plum);display:flex;align-items:center;gap:8px}

.header{position:absolute;left:0;top:41px;width:1200px;height:89px;background:var(--white)}
.brand{position:absolute;left:76px;top:26px;display:flex;align-items:center;gap:12px;font:600 21px "Open Sans",sans-serif;color:var(--plum)}
.brand i{width:36px;height:36px;background:var(--plum);display:block}
.nav{position:absolute;right:79px;top:32px;display:flex;gap:30px;font:400 18px "Roboto Condensed",sans-serif;color:#444;letter-spacing:.3px}
.nav .on{color:#111}

.hero{position:absolute;left:0;top:130px;width:1200px;height:521px;
  background:linear-gradient(180deg,#c9621d 0%,#e39a35 22%,#a9441c 45%,#6b3a1a 62%,#3f4a1f 80%,#5a4a22 100%)}
.hero h1{position:absolute;left:0;right:0;top:228px;text-align:center;font:400 66px "Bebas Neue",sans-serif;color:#fff;letter-spacing:1.5px}

.about h2,.news h2,.contact h2{font:400 41px "Raleway",sans-serif;color:#2d2d2d;text-align:center}
.about h2{position:absolute;left:0;right:0;top:672px}
.copy{position:absolute;left:79px;top:752px;width:1042px}
.copy p{font-size:15px;line-height:26px;margin-bottom:26px}
.copy strong{color:var(--ink)}
.copy strong b{color:var(--plum)}
.photo{float:right;margin:5px 0 20px 40px;width:425px;height:275px;border:5px solid #c8c8c8;
  background:linear-gradient(180deg,#b9c6d8 0%,#8ba0b6 30%,#7a3a2a 55%,#4f7a34 75%,#3f6a2a 100%)}
.copy .after{clear:both}

.communities{position:absolute;left:0;top:1333px;width:1200px;height:156px;background:var(--band);
  display:flex;justify-content:space-around;align-items:center;padding:0 50px}
.communities span{font:600 20px "Open Sans",sans-serif;color:var(--ink)}

.news h2{position:absolute;left:0;right:0;top:1532px}
.item{position:absolute;top:1605px;display:flex;gap:13px;width:330px}
.date{width:70px;height:82px;background:#e4e4e4;text-align:center;padding-top:8px;flex:none}
.date b{display:block;font:600 31px "Open Sans",sans-serif;color:var(--ink);line-height:38px}
.date small{font-size:16px;color:#777}
.item p{font-size:14px;line-height:25px;color:var(--text);width:240px}
.item a{display:block;font:700 14px "Open Sans",sans-serif;color:var(--plum);text-decoration:none;line-height:25px}

.contact{position:absolute;left:0;top:1749px;width:1200px;height:449px;background:var(--soft)}
.contact h2{position:absolute;left:0;right:0;top:36px}
.field{position:absolute;background:#fff;border:1px solid #cfcfcf;font-size:15px;color:#666;padding:10px 10px}
.submit{position:absolute;left:511px;top:335px;width:176px;height:46px;background:var(--plum);color:#fff;
  font:700 20px "Raleway",sans-serif;display:flex;align-items:center;justify-content:center;letter-spacing:.5px}

.footer{position:absolute;left:0;top:2198px;width:1200px;height:183px;background:var(--footer);border-top:5px solid var(--plum)}
.fnav{position:absolute;left:80px;top:34px;display:flex;gap:22px;font-size:16px;color:#666}
.fnav .on{color:var(--plum)}
.footer .social{position:absolute;right:80px;top:38px}
.rule{position:absolute;left:80px;right:80px;top:78px;height:1px;background:#d0d0d0}
.info{position:absolute;top:103px;display:flex;gap:12px;font-size:15px;line-height:25px;color:#444}
.info svg{flex:none;margin-top:4px}
.legal{position:absolute;left:900px;top:103px;font-size:15px;line-height:25px;color:#666}
.legal b{color:var(--ink)}
</style>
</head>
<body>

<div class="topbar">
  <div class="social" aria-label="Social links"><span></span><span></span><span></span></div>
  <div class="phone">
    <svg width="18" height="18" viewBox="0 0 24 24"><path fill="#44203d" d="M6.6 10.8a15 15 0 0 0 6.6 6.6l2.2-2.2c.3-.3.7-.4 1-.2 1.1.4 2.3.6 3.6.6.6 0 1 .4 1 1V20c0 .6-.4 1-1 1A17 17 0 0 1 3 4c0-.6.4-1 1-1h3.5c.6 0 1 .4 1 1 0 1.3.2 2.5.6 3.6.1.3 0 .7-.2 1z"/></svg>
    541-555-0142
  </div>
</div>

<header class="header">
  <div class="brand"><i></i>Fenwick Holdings Corporation</div>
  <nav class="nav"><span class="on">HOME</span><span>ABOUT</span><span>SERVICES</span><span>RESOURCES</span><span>MAP</span><span>BLOG</span><span>CONTACT</span></nav>
</header>

<section class="hero" role="img" aria-label="Sunset over red rock cliffs with pine forest and a river in Central Oregon">
  <h1>Long History , Strong Future</h1>
</section>

<section class="about">
  <h2>About Ridgeway</h2>
  <div class="copy">
    <div class="photo" role="img" aria-label="Historic brick courthouse with clock tower behind autumn trees and a lawn"></div>
    <p>There’s something about the West that still inspires freedom and possibility. Wild rivers and rugged mountains reveal a landscape that’s still evolving. Expansive skies suggest days without limits. And towns like Prineville, in Central Oregon, attract free spirits, who share a love of the land and a desire to build their own lives their own way. It’s this frontier legacy that’s sparked the creation of Ridgeway, a new mixed-use community within the city limits of Prineville.</p>
    <p>Located on the site of a former working ranch and tucked up against dramatic Barnes Butte, Ridgeway is a natural extension of Prineville, promising new places for people to connect with friends, family and the outdoors.</p>
    <p class="after">Ultimately, Ridgeway will evolve into a complete, mixed-use community, with parks, potentially a school and a fire station, and even shops, cafés and other neighborhood amenities. Streets and trails will connect neighborhoods, parks and open spaces, and will provide long-awaited access to public land atop adjacent Barnes Butte.</p>
    <p>If you are interested in obtaining more information about this exciting development, please contact us at 541-555-0142. Or, send an email and we’ll be sure to respond to your questions and comments right away.</p>
    <p><strong>For more information, visit the <b>Ridgeway website</b>.</strong></p>
  </div>
</section>

<section class="communities" aria-label="Communities">
  <span>Ridgeway</span><span>Stone Rim</span><span>Westgate Commons</span><span>Pine Hollow</span><span>Summit Lodge Village</span>
</section>

<section class="news">
  <h2>Latest News</h2>
  <div class="item" style="left:76px">
    <div class="date"><b>30</b><small>Nov</small></div>
    <div><p>Dan Marsh Returns to Fenwick as President and CEO</p><a>READ MORE</a></div>
  </div>
  <div class="item" style="left:443px">
    <div class="date"><b>05</b><small>Dec</small></div>
    <div><p>View of Mt Jefferson and Black Butte on 2015 Fenwick Holdings Annual Wall Calendar</p><a>READ MORE</a></div>
  </div>
  <div class="item" style="left:810px">
    <div class="date"><b>10</b><small>Oct</small></div>
    <div><p>New Pine Hollow Website Launches</p><a>READ MORE</a></div>
  </div>
</section>

<section class="contact">
  <h2>Get In Touch With Us</h2>
  <div class="field" style="left:278px;top:106px;width:311px;height:40px">Enter Name</div>
  <div class="field" style="left:611px;top:106px;width:311px;height:40px">Enter Contact No.</div>
  <div class="field" style="left:278px;top:168px;width:644px;height:40px">Enter Email</div>
  <div class="field" style="left:278px;top:232px;width:644px;height:81px">Enter Email</div>
  <div class="submit">SUBMIT</div>
</section>

<footer class="footer">
  <nav class="fnav"><span class="on">Home</span><span>About</span><span>Development</span><span>Sales</span><span>Vacation rentals</span><span>Owner resources</span><span>Map</span><span>Blog</span><span>Contact</span></nav>
  <div class="social" aria-label="Social links"><span></span><span></span><span></span></div>
  <div class="rule"></div>
  <div class="info" style="left:80px">
    <svg width="13" height="18" viewBox="0 0 12 18"><path fill="#333" d="M6 0a6 6 0 0 0-6 6c0 4.5 6 12 6 12s6-7.5 6-12a6 6 0 0 0-6-6zm0 8.5A2.5 2.5 0 1 1 6 3.5a2.5 2.5 0 0 1 0 5z"/></svg>
    <div>212 NW Juniper Street<br>Bend, Oregon 97701</div>
  </div>
  <div class="info" style="left:349px">
    <svg width="18" height="18" viewBox="0 0 24 24"><path fill="#333" d="M6.6 10.8a15 15 0 0 0 6.6 6.6l2.2-2.2c.3-.3.7-.4 1-.2 1.1.4 2.3.6 3.6.6.6 0 1 .4 1 1V20c0 .6-.4 1-1 1A17 17 0 0 1 3 4c0-.6.4-1 1-1h3.5c.6 0 1 .4 1 1 0 1.3.2 2.5.6 3.6.1.3 0 .7-.2 1z"/></svg>
    <div>541-555-0142</div>
  </div>
  <div class="info" style="left:619px">
    <svg width="18" height="18" viewBox="0 0 18 18"><rect x="1" y="6" width="16" height="11" rx="1" fill="#333"/><rect x="4" y="1" width="10" height="6" fill="none" stroke="#333" stroke-width="1.6"/><rect x="5" y="10" width="8" height="1.6" fill="#e8e8e8"/><rect x="5" y="13" width="8" height="1.6" fill="#e8e8e8"/></svg>
    <div>541-555-0187</div>
  </div>
  <div class="legal">© <b>Fenwick Holdings Corporation.</b><br>All Rights Reserved 2016.</div>
</footer>

</body>
</html>
```